Membership Certificate for Chamber of Commerce Member

I am looking for a certificate to present to Chamber of Commerce Members that showcases their annual membership. The certificate will be placed in frame. I have attached a sample image of the frame from another Chamber of Commerce. I have also attached a proof of the frame that shows our logo at the top and the words "Working Together for a Stronger Community" at the bottom. The certificate should be 7" wide by 5" high. It should say Proud Chamber Member and the year, 2022. I have attached two versions of our logo. I am open to any further suggestions.

Target Market(s)

Business owners/managers

Requirements
Must have
• Year, Proud Chamber Member
Nice to have
• Colors and design that fit our logo and branding. Our website is www.thebrenvillechamber.com.

```html
<!DOCTYPE html>
<html lang="en">
<head>
<meta charset="utf-8">
<title>Proud Chamber Member 2022 – Brenville Chamber</title>
<link href="https://fonts.googleapis.com/css2?family=Asap+Condensed:ital,wght@0,400;0,500;1,700&family=Tinos&display=swap" rel="stylesheet">
<style>
  :root {
    --page-bg: #000000;
    --metal-dark: #6a6a6a;
    --metal-mid: #9a9a9a;
    --metal-light: #d2d2d2;
    --metal-rule: #e6e6e6;
    --paper: #ffffff;
    --navy: #0b1a5e;
    --royal: #2a3a9a;
    --sky: #2e8fd8;
    --orange: #f6921e;
    --silver: #c4c6c8;
    --green: #3cb54a;
    --ink-grey: #5a5a5a;
    --rule-grey: #9a9a9a;
    --band-text: #ffffff;
  }
  html, body {
    margin: 0;
    padding: 0;
    width: 1200px;
    height: 1200px;
    overflow: hidden;
    background: var(--page-bg);
  }
  .plaque {
    display: block;
    width: 1200px;
    height: 1200px;
  }
  .band-name {
    font-family: "Asap Condensed", sans-serif;
    font-weight: 500;
    fill: var(--band-text);
  }
  .seal-name {
    font-family: "Asap Condensed", sans-serif;
    font-weight: 500;
    fill: var(--ink-grey);
  }
  .headline {
    font-family: "Asap Condensed", sans-serif;
    font-weight: 500;
  }
  .presented-to {
    font-family: "Asap Condensed", sans-serif;
    font-weight: 400;
    fill: var(--ink-grey);
  }
  .year {
    font-family: "Asap Condensed", sans-serif;
    font-weight: 700;
    font-style: italic;
    fill: var(--orange);
  }
  .recipient {
    font-family: "Asap Condensed", sans-serif;
    font-weight: 400;
    fill: var(--ink-grey);
    word-spacing: 6px;
  }
  .field-label {
    font-family: "Asap Condensed", sans-serif;
    font-weight: 400;
    fill: var(--ink-grey);
  }
  .motto {
    font-family: "Tinos", serif;
    fill: var(--band-text);
  }
</style>
</head>
<body>
<svg class="plaque" viewBox="0 0 980 980" xmlns="http://www.w3.org/2000/svg" aria-labelledby="plaque-title">
  <title id="plaque-title">Proud Chamber Member 2022 certificate in a metal plaque frame</title>
  <defs>
    <linearGradient id="metal" x1="0" y1="0" x2="1" y2="0">
      <stop offset="0" stop-color="var(--metal-dark)"/>
      <stop offset="0.5" stop-color="var(--metal-light)"/>
      <stop offset="1" stop-color="var(--metal-dark)"/>
    </linearGradient>
    <linearGradient id="side-art-tone" x1="0" y1="0" x2="1" y2="1">
      <stop offset="0" stop-color="var(--navy)"/>
      <stop offset="0.45" stop-color="var(--royal)"/>
      <stop offset="0.75" stop-color="var(--sky)"/>
      <stop offset="1" stop-color="var(--silver)"/>
    </linearGradient>
    <linearGradient id="corner-art-tone" x1="0" y1="0" x2="1" y2="1">
      <stop offset="0" stop-color="var(--green)"/>
      <stop offset="1" stop-color="var(--royal)"/>
    </linearGradient>
    <linearGradient id="headline-ink" x1="0" y1="0" x2="1" y2="0">
      <stop offset="0" stop-color="var(--sky)"/>
      <stop offset="0.5" stop-color="var(--royal)"/>
      <stop offset="1" stop-color="var(--sky)"/>
    </linearGradient>
  </defs>

  <rect class="plaque-base" x="88" y="92" width="808" height="808" fill="var(--metal-mid)"/>

  <g class="top-band">
    <rect x="88" y="92" width="808" height="113" fill="url(#metal)"/>
    <rect x="100" y="101" width="784" height="95" fill="none" stroke="var(--metal-rule)" stroke-width="1.5"/>
    <circle cx="398" cy="149" r="9" fill="var(--band-text)"/>
    <text class="band-name" x="416" y="156" font-size="20">Brenville Chamber of Commerce &amp; Tourism</text>
  </g>

  <g class="certificate">
    <rect x="96" y="213" width="791" height="565" fill="var(--paper)"/>

    <path class="side-art" role="img" aria-label="Decorative sweeping bands in navy, blue, orange and silver"
          d="M96,213 L560,213 C420,250 330,320 300,430 C280,520 220,650 96,770 Z"
          fill="url(#side-art-tone)" opacity="0.9"/>
    <path class="corner-art" role="img" aria-label="Decorative corner bands in green, silver and blue"
          d="M720,778 C780,720 840,690 887,675 L887,778 Z"
          fill="url(#corner-art-tone)" opacity="0.85"/>

    <rect class="inner-rule" x="113" y="230" width="763" height="532" fill="none" stroke="var(--sky)" stroke-width="2"/>

    <g class="chamber-seal">
      <circle cx="785" cy="323" r="66" fill="var(--paper)" stroke="var(--silver)" stroke-width="2"/>
      <text class="seal-name" x="785" y="330" text-anchor="middle" font-size="20">Brenville</text>
    </g>

    <text class="headline" x="427" y="407" font-size="56" fill="url(#headline-ink)">PROUD</text>
    <text class="headline" x="427" y="467" font-size="56" fill="url(#headline-ink)">CHAMBER MEMBER</text>
    <text class="presented-to" x="428" y="503" font-size="25">PRESENTED TO</text>
    <text class="year" x="843" y="530" text-anchor="end" font-size="64">2022</text>

    <text class="recipient" x="628" y="638" text-anchor="middle" font-size="52">Name Surname</text>
    <line x1="420" y1="648" x2="845" y2="648" stroke="var(--rule-grey)" stroke-width="1.5"/>

    <line x1="218" y1="724" x2="403" y2="724" stroke="var(--rule-grey)" stroke-width="1.2"/>
    <text class="field-label" x="219" y="746" font-size="15">DATE</text>
    <line x1="421" y1="724" x2="606" y2="724" stroke="var(--rule-grey)" stroke-width="1.2"/>
    <text class="field-label" x="422" y="746" font-size="15">SIGNATURE</text>
  </g>

  <g class="bottom-band">
    <rect x="88" y="785" width="808" height="115" fill="url(#metal)"/>
    <rect x="100" y="795" width="784" height="95" fill="none" stroke="var(--metal-rule)" stroke-width="1.5"/>
    <text class="motto" x="490" y="836" text-anchor="middle" font-size="27">WORKING TOGETHER</text>
    <text class="motto" x="490" y="868" text-anchor="middle" font-size="27">FOR A STRONGER COMMUNITY</text>
  </g>
</svg>
</body>
</html>
```